SkyvornQ Business Cards and Stationary Design

Need a design for our business cards and stationary. I want to carry on the theme of the logo. I want the business cards to have a design on the back. I would like the business cards and the stationary to carry the same theme, design scheme, and branding

Target Market(s)

Airlines and Maintenance Facilities

Industry/Entity Type

Aviation

Contact Information for Business Card

Address: 4827 Tallowmere Lane, Larkhaven, Ostrel, 34951

Font styles to use
Serif
Sans Serif

Colors

Designer to choose colors to be used in the design.

```html
<!DOCTYPE html>
<html lang="en">
<head>
<meta charset="utf-8">
<title>SkyvornQ Business Card</title>
<link href="https://fonts.googleapis.com/css2?family=Roboto:wght@400;500;700&family=Montserrat:wght@700&display=swap" rel="stylesheet">
<style>
  :root {
    --backdrop: #2e2e2e;
    --navy: #0b2650;
    --navy-deep: #08214a;
    --blue-bright: #0aa6e6;
    --blue-mid: #0f6fbf;
    --blue-dark: #0d3f86;
    --paper: #f1f1f1;
    --white: #ffffff;
  }
  * { box-sizing: border-box; margin: 0; padding: 0; }
  html, body { width: 1200px; height: 960px; overflow: hidden; }
  body {
    background: var(--backdrop);
    position: relative;
    font-family: "Roboto", Arial, sans-serif;
  }
  .card {
    position: absolute;
    width: 600px;
    height: 342px;
    border-radius: 18px;
    overflow: hidden;
  }
  .card-front { left: 313px; top: 113px; background: var(--paper); }
  .card-back { left: 311px; top: 472px; background: var(--navy-deep); }
  .front-art { position: absolute; inset: 0; }
  .contact-block {
    position: absolute;
    left: 35px;
    top: 142px;
    color: var(--white);
  }
  .person-name { font-weight: 500; font-size: 21px; line-height: 24px; letter-spacing: 0.2px; }
  .person-title { font-weight: 500; font-size: 15px; line-height: 18px; }
  .address { margin-top: 12px; font-size: 15px; line-height: 18.5px; font-style: normal; }
  .contact-list { list-style: none; margin-top: 9px; }
  .contact-list li {
    display: flex; align-items: center;
    font-size: 15px; line-height: 19px;
  }
  .contact-list svg { width: 15px; height: 15px; margin-right: 8px; fill: var(--white); flex: none; }
  .brand-front {
    position: absolute;
    left: 300px; top: 40px; width: 270px;
    display: flex; flex-direction: column; align-items: center;
  }
  .brand-ring {
    width: 82px; height: 82px; border-radius: 50%;
    border: 8px solid var(--blue-dark);
  }
  .brand-name {
    font-family: "Montserrat", Arial, sans-serif;
    font-weight: 700;
  }
  .brand-front .brand-name {
    margin-top: 14px; font-size: 27px; letter-spacing: 3.5px; color: var(--navy);
  }
  .brand-back {
    position: absolute; left: 0; right: 0; top: 76px;
    display: flex; flex-direction: column; align-items: center;
  }
  .brand-back .brand-ring { width: 150px; height: 150px; border: 12px solid var(--white); }
  .brand-back .brand-name {
    margin-top: 14px; font-size: 22px; letter-spacing: 4px; color: var(--white);
  }
  .website-back {
    position: absolute; left: 0; right: 0; top: 289px;
    text-align: center; color: var(--white);
    font-size: 14px; letter-spacing: 6.5px;
  }
</style>
</head>
<body>
  <section class="card card-front">
    <svg class="front-art" viewBox="0 0 600 342" aria-hidden="true">
      <defs>
        <radialGradient id="panelGlow" cx="0.5" cy="0.48" r="0.75">
          <stop offset="0" stop-color="#0aa6e6"/>
          <stop offset="0.5" stop-color="#0f6fbf"/>
          <stop offset="1" stop-color="#0d3f86"/>
        </radialGradient>
      </defs>
      <path d="M0,0 L167,0 C230,150 330,300 472,342 L0,342 Z" fill="url(#panelGlow)"/>
      <path d="M172,0 C236,150 336,296 478,342 L552,342 C380,320 250,200 172,0 Z" fill="#0b2650"/>
      <path d="M167,0 C230,150 330,300 472,342" fill="none" stroke="#ffffff" stroke-width="3"/>
    </svg>

    <div class="brand-front">
      <div class="brand-ring"></div>
      <div class="brand-name">SKYVORNQ</div>
    </div>

    <div class="contact-block">
      <div class="person-name">DORIAN VALE</div>
      <div class="person-title">CEO/FOUNDER</div>
      <address class="address">4827 Tallowmere Lane<br>Larkhaven, Ostrel, 34951</address>
      <ul class="contact-list">
        <li><svg viewBox="0 0 24 24"><path d="M6.6 10.8a15.1 15.1 0 0 0 6.6 6.6l2.2-2.2c.3-.3.7-.4 1-.2 1.1.4 2.3.6 3.6.6.6 0 1 .4 1 1V20c0 .6-.4 1-1 1A17 17 0 0 1 3 4c0-.6.4-1 1-1h3.5c.6 0 1 .4 1 1 0 1.3.2 2.5.6 3.6.1.3 0 .7-.2 1z"/></svg>555 210 7384</li>
        <li><svg viewBox="0 0 24 24"><path d="M7 1h10a2 2 0 0 1 2 2v18a2 2 0 0 1-2 2H7a2 2 0 0 1-2-2V3a2 2 0 0 1 2-2zm0 3v14h10V4zm5 15.5a1.2 1.2 0 1 0 0 2.4 1.2 1.2 0 0 0 0-2.4z"/></svg>555 864 1926</li>
        <li><svg viewBox="0 0 24 24"><path d="M2 5h20v14H2zm2 2v.5l8 5 8-5V7l-8 5z"/></svg>info@skyvornq.com</li>
        <li><svg viewBox="0 0 24 24"><path d="M12 2a10 10 0 1 0 0 20 10 10 0 0 0 0-20zm-1 17.9A8 8 0 0 1 4.2 10l4.8 4.8v1a2 2 0 0 0 2 2zm6.9-2.5A2 2 0 0 0 16 16h-1v-3a1 1 0 0 0-1-1H8v-2h2a1 1 0 0 0 1-1V7h2a2 2 0 0 0 2-2v-.4a8 8 0 0 1 2.9 12.8z"/></svg>www.skyvornq.com</li>
      </ul>
    </div>
  </section>

  <section class="card card-back">
    <div class="brand-back">
      <div class="brand-ring"></div>
      <div class="brand-name">SKYVORNQ</div>
    </div>
    <div class="website-back">www.skyvornq.com</div>
  </section>
</body>
</html>
```